Business card design needed

Family General Practitioner/ Family Physician.
Logo is the logo of the Imperial Guild of Community Clinicians Oceania
http://pkvtm.lorimar.example/PictureGallery/logos/pages/IGCCO%20logo_jpg.htm

Reason: Just a bit more time to make changes and the weekend for me to look at things closely and to choose. Thanks, Ulan

Thanks for all the submissions. So many of them are really works of art. Not one of them are not good. The ones that I am eliminating are the ones that I think are not suitable for me personally only, and because if I don't, it makes it very difficult to decide as many of you are also sending me slight variations of a card. I have just decided to choose a second place card too. Can't thank you all enough. Good luck, Ulan. P.S - Working today till 10 pm as the card says :-), so probably won't be able to give a feedback till late Saturday night or Sunday morning here in Sydney, Australia. 

Reason: Just added a second place to the budget and realised that Australia is ahead of the rest of the world in the time zone (only :-) - don't want to offend anyone or start a debate!! ) , so Monday deadline will mean it will be a weekend for the rest of the world. Just wanted to give everyone more time to submit their best, especially since I will be picking a second card too. Can't thank everyone enough for the submissions. P.S - Not keen on photos on the card.

Business

Contact Information for Business Card

Dr. Ulan Pereira M.B.B.S., F.I.G.C.C.O
Family General Practitioner
Address, timings, phone and fax number on the back.

Requirements
Must have
• Timings
Mon 7 am - 7 pm
Tues 7 am - 12 pm
Wed 7 am - 10 pm
Thurs 7 am - 12 pm
Fri 7 am - 8 pm
Sat 8 am - 10 pm
Sun - Off

```html
<!DOCTYPE html>
<html lang="en">
<head>
<meta charset="utf-8">
<title>Business Card Back – Opening Hours and Contact</title>
<link rel="stylesheet" href="https://fonts.googleapis.com/css2?family=Michroma&family=PT+Sans&display=swap">
<style>
  :root {
    --card-bg: #363533;
    --card-bg-mid: #2e2d2c;
    --card-bg-deep: #242322;
    --hours-band: rgba(214, 208, 196, 0.68);
    --hours-ink: #24221f;
    --contact-ink: #ffffff;
  }
  html, body {
    margin: 0;
    padding: 0;
    width: 1200px;
    height: 646px;
    overflow: hidden;
    background: var(--card-bg-mid);
  }
  .card {
    position: relative;
    width: 1200px;
    height: 646px;
    overflow: hidden;
  }
  .card__texture {
    position: absolute;
    inset: 0;
    background:
      radial-gradient(ellipse at 45% 45%, var(--card-bg) 0%, var(--card-bg-mid) 60%, var(--card-bg-deep) 100%);
  }
  .hours {
    position: absolute;
    left: 3px;
    top: 0;
    margin: 0;
    padding: 0;
    list-style: none;
    font-family: "PT Sans", sans-serif;
    font-size: 25px;
    letter-spacing: -0.3px;
    color: var(--hours-ink);
  }
  .hours__day {
    position: absolute;
    left: 0;
    height: 31px;
    line-height: 31px;
    background: var(--hours-band);
    text-align: right;
    padding-right: 7px;
    box-sizing: border-box;
    white-space: nowrap;
    display: flex;
    justify-content: flex-end;
  }
  .hours__day--mon { top: 67px;  width: 271px; }
  .hours__day--tue { top: 110px; width: 238px; }
  .hours__day--wed { top: 156px; width: 289px; }
  .hours__day--thu { top: 199px; width: 372px; }
  .hours__day--fri { top: 242px; width: 212px; }
  .hours__day--sat { top: 286px; width: 278px; }
  .hours__day--sun { top: 335px; width: 221px; }
  .contact {
    position: absolute;
    left: 687px;
    top: 423px;
    margin: 0;
    font-family: "Michroma", sans-serif;
    font-style: normal;
    text-transform: uppercase;
    color: var(--contact-ink);
    font-size: 19px;
    letter-spacing: 2px;
    line-height: 39px;
    white-space: nowrap;
    -webkit-text-stroke: 0.7px var(--contact-ink);
  }
  .contact__line { display: block; }
  .contact__initial { font-size: 25px; }
</style>
</head>
<body>
  <main class="card">
    <div class="card__texture" role="img" aria-label="Dark grey leopard-print texture covering the whole card"></div>

    <ul class="hours" aria-label="Opening hours">
      <li class="hours__day hours__day--mon">Mon 7 am - 7 pm</li>
      <li class="hours__day hours__day--tue">Tues 7 am - 12 pm</li>
      <li class="hours__day hours__day--wed">Wed 7 am - 10 pm</li>
      <li class="hours__day hours__day--thu">Thurs 7 am - 12 pm</li>
      <li class="hours__day hours__day--fri">Fri 7 am - 8 pm</li>
      <li class="hours__day hours__day--sat">Sat 8 am - 10 pm</li>
      <li class="hours__day hours__day--sun">Sun - Off</li>
    </ul>

    <address class="contact">
      <span class="contact__line"><span class="contact__initial">C</span>ontact:</span>
      <span class="contact__line">phone: xxxxxxxxxx</span>
      <span class="contact__line">fax number:xxxxxxxxxx</span>
    </address>
  </main>
</body>
</html>
```